Poster Design Job - Winner can do follow-up business

- Varundo.com is a Swiss-based online store selling business shirts and accessories for business men
- Please visit the webpage to make yourself familiar with the company. Although the text is in German, with Google translator you should be able to understand the main content.
- Our clients are mainly business men between 30 and 60 years old. Mostly with a high income working in the service industry (banking, insurance, lawyers, etc.). Sometimes there wives purchase the shirts for them ;-)
- The colors and the logo are given, as they are also used for the print materials (please see files in attachment)
- I am running several businesses and often need a talented web designer --> the winner gets substantial follow-up business
your task:
- For our company we need a poster for a larger billboard advertisement campaign. We plan to book billboard space all over Switzerland.
- Please include in the poster the logo & the claim "Das Perfekte Hemd für jeden" "Passend | Einfach | Garantierte Qualität" in english this means "The perfect shirt for everybody" "Fitting | Simple | Guaranteed Quality"
- Also you need to include the following text - don`t change it:
Frühlingsaktion 20 Franken Gutschein für Ihr erstes Varundo-Hemd auf www.varundo.com. Gutscheincode: Frühling
-The text means: Spring Sale 20 CHF off for your first Varundo shirt on www.varundo.com. Your coupon code: Spring
-Don`t change the Logo or our corporate colors
-All images that are on the website are available. Please just ask kp@varundo.com!
- Format should be A0 - 841 x 1189mm - Portrait
Updates
Project Deadline Extended
Reason: Need some more time to work on the designs handed in by the designers.
Best,
Bertrand

```html
<!DOCTYPE html>
<html lang="de">
<head>
<meta charset="utf-8">
<title>Varundo – Frühlingsaktion Plakat</title>
<link rel="stylesheet" href="https://fonts.googleapis.com/css2?family=Montserrat:wght@500&family=Open+Sans:wght@600;700&family=Roboto:wght@400&display=swap">
<style>
  :root {
    --stage: #1b2026;
    --paper: #ffffff;
    --brand-red: #e8332a;
    --brand-gold: #e2cf6b;
    --ink-dark: #0b0b0c;
    --text-light: #ffffff;
    --fabric-light: #8c8f8c;
    --fabric-mid: #3b3d3c;
  }
  * { box-sizing: border-box; margin: 0; padding: 0; }
  html, body {
    width: 756px;
    height: 1200px;
    overflow: hidden;
    background: var(--stage);
  }
  .poster {
    position: absolute;
    left: 0;
    top: 65px;
    width: 756px;
    height: 1069px;
    background: var(--ink-dark);
    overflow: hidden;
  }
  .brand-area {
    position: absolute;
    left: 0; top: 0;
    width: 100%;
    height: 367px;
    background: var(--paper);
  }
  .brand-mark {
    position: absolute;
    left: 348px;
    top: 80px;
    width: 60px;
    height: 60px;
    background: var(--brand-red);
  }
  .brand-name {
    position: absolute;
    left: 0; right: 0;
    top: 222px;
    text-align: center;
    font-family: "Montserrat", sans-serif;
    font-weight: 500;
    font-size: 112px;
    line-height: 1;
    letter-spacing: 4px;
    color: var(--brand-gold);
  }
  .claim-band {
    position: absolute;
    left: 0; top: 367px;
    width: 100%;
    height: 109px;
    background: var(--brand-red);
    color: var(--text-light);
    font-family: "Roboto", sans-serif;
    text-align: center;
  }
  .claim-headline {
    padding-top: 16px;
    font-size: 33px;
    line-height: 1.1;
    letter-spacing: 0.3px;
  }
  .claim-values {
    margin-top: 10px;
    font-size: 27px;
    line-height: 1.1;
    display: flex;
    justify-content: center;
    align-items: center;
  }
  .claim-divider {
    display: inline-block;
    width: 2px;
    height: 28px;
    margin: 0 16px;
    background: var(--brand-gold);
  }
  .hero-photo {
    position: absolute;
    left: 0; top: 476px;
    width: 100%;
    height: 593px;
    background:
      radial-gradient(ellipse 55% 60% at 55% 45%, var(--fabric-light) 0%, var(--fabric-mid) 45%, transparent 75%),
      var(--ink-dark);
  }
  .offer {
    position: absolute;
    left: 49px;
    top: 525px;
    color: var(--text-light);
    font-family: "Open Sans", sans-serif;
  }
  .offer-details {
    font-size: 12px;
    font-weight: 600;
    line-height: 18px;
  }
  .offer-url {
    margin-top: 3px;
    font-size: 22px;
    font-weight: 700;
    color: var(--brand-red);
    line-height: 1.2;
  }
  .offer-code {
    font-size: 19px;
    font-weight: 700;
    line-height: 1.35;
  }
</style>
</head>
<body>
  <main class="poster">
    <header class="brand-area">
      <div class="brand-mark"></div>
      <h1 class="brand-name">VARUNDO</h1>
    </header>

    <section class="claim-band">
      <p class="claim-headline">DAS PERFEKTE HEMD FÜR JEDEN</p>
      <p class="claim-values">
        <span>Passend</span><span class="claim-divider"></span><span>Einfach</span><span class="claim-divider"></span><span>Garantierte Qualität</span>
      </p>
    </section>

    <div class="hero-photo" role="img" aria-label="Nahaufnahme einer strukturierten grauen Krawatte mit Knoten auf schwarzem Grund"></div>

    <section class="offer">
      <p class="offer-details">Frühlingsaktion 20 Franken Gutschein<br>für Ihr erstes Varundo-Hemd auf</p>
      <p class="offer-url">www.varundo.com.</p>
      <p class="offer-code">Gutscheincode: Frühling</p>
    </section>
  </main>
</body>
</html>
```